New product logo and packaging design for brand ( Nestwell & Rinse)

I need a logo and packaging design for 2 new products that will look similar. One is eco friendly dishwashing sheets and the other is a eco friendly dishwashing sheets.
The descriptions that go on the boxes have all ready been written and I have uploaded for you to utilise on the back of the box,. Please search eco washing sheets on google for brand references.
The look should be upmarket but yet show to be eco friendly. The brand will be called Nestwell & Rinse. Feel free to let your creative juices flow and make something you believe would work well and doesn't look like our competitors. It should look clean yet incorporate something natural with an animal.
I like the artwork for https://velmorastone.example/ but don't make it look the same.
Possibly the outline of the planet earth inside the letter O in nestwell & rinse logo.

The laundry sheets are:
OCEAN BREEZE

The Dishwasher sheets are:
LEMON
I repeat , they should NOT look like the competitors.

Must use the template for the design in the attached files!

On the front should say - 80 Sheets

There will be a second contest I will post now that will be the same project under a different name you can search it and enter both if you would like, they will be sold at different price points to attract different customers.

I have uploaded a new template , the manufacturer gave me the wrong template please update asap

Washing clothes

• use the template for the design in the attached files

```html
<!DOCTYPE html>
<html lang="en">
<head>
<meta charset="utf-8">
<title>Nestwell &amp; Rinse – Ocean Breeze Dieline</title>
<link rel="stylesheet" href="https://fonts.googleapis.com/css2?family=Lexend:wght@300;400;500;600;700&family=Marcellus&family=Italiana&display=swap">
<style>
  :root{
    --bg:#dcdcdc;
    --paper:#ffffff;
    --panel-teal:#9fd4d0;
    --panel-light:#d0e9e1;
    --ink-teal:#1a7f88;
    --text-teal:#2a9aa0;
    --deep-green:#344d38;
    --label-white:#f5f5f5;
    --black:#0a0a0a;
    --dim-red:#e01010;
    --cut:#1d2a2a;
  }
  *{margin:0;padding:0;box-sizing:border-box}
  html,body{width:1200px;height:1200px;overflow:hidden;background:var(--bg)}
  .artboard{position:absolute;left:0;top:0;width:1932px;height:1932px;transform:scale(0.62112);transform-origin:0 0;font-family:"Lexend",sans-serif;color:var(--text-teal)}
  .dieline{position:absolute;left:0;top:0}
  .abs{position:absolute}
  .glue-zone{position:absolute;background:var(--paper) repeating-linear-gradient(135deg,transparent 0 14px,var(--black) 14px 16px);}
  .heading{font-weight:600;color:var(--ink-teal);font-size:12px;letter-spacing:.1px;white-space:nowrap}
  .body{font-weight:300;font-size:11.2px;line-height:14.7px;color:var(--text-teal)}
  .body.justify{text-align:justify}
  .sub{font-weight:500;color:var(--ink-teal);font-size:12px}
  .ingredient-list{list-style:none;font-weight:300;font-size:10.6px;line-height:13.1px;white-space:nowrap}
  .ingredient-list li::before{content:"• "}
  .illus{position:absolute;background:linear-gradient(180deg,#bfe0d8,#a9d6cf);border-radius:4px}
  .code-tile{position:absolute;background:var(--ink-teal)}
  .contact{position:absolute;display:flex;align-items:center;gap:6px;font-weight:600;font-size:12px;color:var(--ink-teal);white-space:nowrap}
  .contact .mark{width:15px;height:15px;border:1.4px solid var(--ink-teal);border-radius:3px}
  .storage{font-weight:600;font-size:11.6px;line-height:14.8px;color:var(--ink-teal)}
  .expiry-box{position:absolute;border-radius:12px;background:var(--deep-green)}
  .batch-box{position:absolute;background:var(--label-white)}
  .brand-name{position:absolute;font-family:"Lexend",sans-serif;font-weight:500;font-size:21px;line-height:20px;color:var(--black);letter-spacing:-.4px;white-space:nowrap}
  .product-tag{position:absolute;background:var(--black);color:#fff;font-weight:300;font-size:19px;letter-spacing:.3px;white-space:nowrap;display:flex;align-items:center;justify-content:center}
  .wave-band{position:absolute;background:linear-gradient(180deg,rgba(42,154,160,.15),rgba(42,154,160,.35),rgba(42,154,160,.15));border-radius:20px}
  .scent-name{position:absolute;font-family:"Marcellus",serif;color:var(--text-teal);font-size:66px;line-height:50px;letter-spacing:3px}
  .count-number{position:absolute;font-family:"Italiana",serif;color:var(--ink-teal);font-size:76px;line-height:60px}
  .count-label{position:absolute;background:var(--ink-teal);color:#fff;font-weight:300;font-size:17px;display:flex;align-items:center;justify-content:center;letter-spacing:.5px}
  .claim-badge{position:absolute;width:92px;height:92px;border-radius:50%;background:radial-gradient(circle,rgba(42,154,160,.28),rgba(42,154,160,.08))}
  .benefit-strip{position:absolute;background:var(--ink-teal);display:flex;gap:14px;padding:8px 14px;color:#d8efec;font-weight:300;font-size:7.4px;line-height:9.8px}
  .benefit-strip p{flex:1;text-align:justify}
  .dim-label{position:absolute;color:var(--dim-red);font-family:"Lexend",sans-serif;font-weight:300;font-size:38px}
  .dim-label.vertical{transform:translate(-50%,-50%) rotate(-90deg);white-space:nowrap}
</style>
</head>
<body>
<div class="artboard">

  <svg class="dieline" width="1932" height="1932" viewBox="0 0 1932 1932" aria-hidden="true">
    <polygon points="533,340 706,470 1402,470 1573,340 1573,1512 533,1512" fill="var(--paper)"/>
    <polygon points="724,332 1382,332 1402,469 706,469" fill="var(--panel-teal)" stroke="var(--cut)" stroke-width="1.2"/>
    <path d="M970,401 H1030 Q1036,388 1054,388 Q1072,388 1078,401 H1137 a6,6 0 0 1 0,12 H970 a6,6 0 0 1 0,-12 Z" fill="none" stroke="var(--cut)" stroke-width="1.2"/>
    <polygon points="557,489 628,477 706,477 706,904 628,895 557,895" fill="var(--panel-teal)" stroke="var(--cut)" stroke-width="1.2"/>
    <polygon points="1402,477 1480,477 1550,489 1550,895 1480,904 1402,904" fill="var(--panel-teal)" stroke="var(--cut)" stroke-width="1.2"/>
    <rect x="706" y="469" width="696" height="444" fill="var(--panel-light)" stroke="var(--cut)" stroke-width="1.2"/>
    <rect x="555" y="913" width="997" height="155" fill="var(--panel-teal)"/>
    <line x1="706" y1="913" x2="706" y2="1068" stroke="var(--cut)" stroke-width="1.2"/>
    <line x1="1402" y1="913" x2="1402" y2="1068" stroke="var(--cut)" stroke-width="1.2"/>
    <path d="M706,920 H640 A70,70 0 0 0 640,1060 H706" fill="none" stroke="var(--cut)" stroke-width="1.2"/>
    <path d="M1402,920 H1468 A70,70 0 0 1 1468,1060 H1402" fill="none" stroke="var(--cut)" stroke-width="1.2"/>
    <polygon points="555,1087 628,1076 706,1076 706,1505 628,1497 555,1505" fill="var(--panel-teal)" stroke="var(--cut)" stroke-width="1.2"/>
    <polygon points="1402,1076 1480,1076 1552,1087 1552,1505 1480,1497 1402,1505" fill="var(--panel-teal)" stroke="var(--cut)" stroke-width="1.2"/>
    <rect x="706" y="1068" width="696" height="444" fill="var(--panel-light)" stroke="var(--cut)" stroke-width="1.2"/>
    <rect x="555" y="1512" width="997" height="153" fill="var(--panel-teal)"/>
    <line x1="706" y1="1512" x2="706" y2="1665" stroke="var(--cut)" stroke-width="1.2"/>
    <line x1="1402" y1="1512" x2="1402" y2="1665" stroke="var(--cut)" stroke-width="1.2"/>
    <line x1="706" y1="1665" x2="1402" y2="1665" stroke="var(--cut)" stroke-width="1.2"/>
    <path d="M706,1520 H640 A70,70 0 0 0 640,1660 H706" fill="none" stroke="var(--cut)" stroke-width="1.2"/>
    <path d="M1402,1520 H1468 A70,70 0 0 1 1468,1660 H1402" fill="none" stroke="var(--cut)" stroke-width="1.2"/>
    <path d="M775,1078 V1380 Q778,1470 815,1512" fill="none" stroke="var(--cut)" stroke-width="1.2"/>
    <path d="M795,1078 V1380 Q798,1460 825,1512" fill="none" stroke="var(--cut)" stroke-width="1.2"/>
    <path d="M1333,1078 V1380 Q1330,1470 1293,1512" fill="none" stroke="var(--cut)" stroke-width="1.2"/>
    <path d="M1313,1078 V1380 Q1310,1460 1283,1512" fill="none" stroke="var(--cut)" stroke-width="1.2"/>
    <path d="M816,1512 V1600 Q816,1610 826,1610 H965 Q980,1612 980,1630 L930,1665" fill="none" stroke="var(--cut)" stroke-width="1.2" stroke-dasharray="22 6"/>
    <path d="M1292,1512 V1600 Q1292,1610 1282,1610 H1143 Q1128,1612 1128,1630 L1178,1665" fill="none" stroke="var(--cut)" stroke-width="1.2" stroke-dasharray="22 6"/>
    <path d="M980,1630 Q984,1650 1000,1652 H1108 Q1124,1650 1128,1630" fill="none" stroke="var(--cut)" stroke-width="1.2"/>
    <g stroke="var(--dim-red)" stroke-width="1.2">
      <line x1="452" y1="332" x2="452" y2="1665"/>
      <line x1="447" y1="332" x2="520" y2="332"/>
      <line x1="447" y1="469" x2="520" y2="469"/>
      <line x1="447" y1="913" x2="527" y2="913"/>
      <line x1="447" y1="1068" x2="521" y2="1068"/>
      <line x1="447" y1="1512" x2="523" y2="1512"/>
      <line x1="447" y1="1665" x2="523" y2="1665"/>
      <line x1="555" y1="1770" x2="1552" y2="1770"/>
      <line x1="555" y1="1700" x2="555" y2="1775"/>
      <line x1="706" y1="1700" x2="706" y2="1775"/>
      <line x1="1402" y1="1693" x2="1402" y2="1775"/>
      <line x1="1552" y1="1693" x2="1552" y2="1775"/>
    </g>
  </svg>

  <div class="glue-zone" style="left:730px;top:422px;width:210px;height:31px"></div>
  <div class="glue-zone" style="left:1170px;top:422px;width:203px;height:31px"></div>
  <div class="glue-zone" style="left:655px;top:496px;width:32px;height:390px"></div>
  <div class="glue-zone" style="left:1421px;top:496px;width:31px;height:390px"></div>

  <div class="abs heading" style="left:725px;top:486px">HOW TO USE</div>

  <div class="abs" style="left:725px;top:504px;width:213px">
    <div class="sub">For Dishwashers:</div>
    <p class="body justify">• Place a single sheet into your dishwasher's detergent compartment and let it do the work.</p>
  </div>
  <div class="abs" style="left:950px;top:504px;width:207px">
    <div class="sub">For Dish Drawers:</div>
    <p class="body justify">• Tear a sheet in half and place it in the cutlery tray. If you see extra foam, use less next time.</p>
  </div>
  <div class="abs" style="left:1169px;top:504px;width:213px">
    <div class="sub">For Hand Washing:</div>
    <p class="body">• Add one sheet to warm water, let it dissolve, and wash dishes as usual</p>
  </div>

  <div class="illus" role="img" aria-label="Line drawing of a dishwasher with detergent compartment" style="left:790px;top:572px;width:87px;height:64px"></div>
  <div class="illus" role="img" aria-label="Line drawing of a sheet torn in half" style="left:1011px;top:581px;width:84px;height:43px"></div>
  <div class="illus" role="img" aria-label="Line drawing of a sheet dissolving in a bowl of water" style="left:1244px;top:558px;width:55px;height:63px"></div>

  <div class="abs" style="left:725px;top:643px;width:222px">
    <div class="heading">LOAD SIZE GUIDE</div>
    <p class="body" style="white-space:nowrap">• One sheet for full loads or handwashing.</p>
  </div>

  <div class="abs" style="left:725px;top:712px;width:213px">
    <div class="heading">EARTH-FRIENDLY FORMULA</div>
    <p class="body justify">• Free from harsh chemicals like phosphates, dyes, and bleach</p>
    <p class="body justify">• Safe for septic tanks and greywater systems</p>
    <p class="body justify">• 100% plastic-free, biodegradable packaging</p>
    <p class="body">• Made with eco-friendly ingredients</p>
  </div>

  <div class="abs" style="left:950px;top:642px;width:208px">
    <div class="heading">WHAT'S INSIDE</div>
    <p class="sub" style="font-size:11.6px;line-height:14.5px;text-align:justify">We use natural, plant-based ingredients such as:</p>
    <ul class="ingredient-list">
      <li>Sodium Dodecyl Sulphate</li>
      <li>Aqua</li>
      <li>Decyl Glucoside</li>
      <li>PEG-7 Glyceryl Cocoate</li>
      <li>Cocamidopropyl Betaine</li>
      <li>Cocamidopropylamine Oxide</li>
      <li>Coconut Oil Monoethanolamide</li>
      <li>Glycerin</li>
      <li>Alcohols, C12-18, Ethoxylated</li>
      <li>Perfume</li>
      <li>Sodium Carbonate</li>
    </ul>
  </div>

  <div class="abs" style="left:1169px;top:642px;width:213px">
    <div class="heading">OUR PROMISE</div>
    <p class="body justify">At Nestwell &amp; Rinse, we're proud to be an Australian-owned business committed to sustainability. By switching to our dishwashing sheets, you're helping to protect the environment one load at a time.</p>
  </div>
  <div class="code-tile" role="img" aria-label="Scannable code area" style="left:1232px;top:749px;width:79px;height:79px"></div>

  <div class="abs" style="left:725px;top:833px">
    <div class="heading">GET IN TOUCH</div>
    <div class="sub" style="font-weight:600;margin-top:1px;white-space:nowrap">We love hearing from you! Reach out with your questions or feedback:</div>
  </div>

  <div class="contact" style="left:744px;top:876px"><span class="mark"></span>support@nestwellrinse.example</div>
  <div class="contact" style="left:1002px;top:876px"><span class="mark"></span>www.nestwellrinse.example</div>
  <div class="contact" style="left:1252px;top:876px"><span class="mark"></span>@nestwellrinse</div>

  <div class="abs heading" style="left:725px;top:935px">STORAGE AND SHELF LIFE</div>
  <div class="abs storage" style="left:725px;top:964px;width:440px">
    <p>• Store in a cool, dry place away from direct sunlight.</p>
    <p>• Close the box tightly after each use to maintain freshness.</p>
    <p>• Shelf life: 2 years from the production date (see box for details).</p>
    <p style="margin-top:14.8px">CAUTION: Do not ingest. Keep out of eyes. If contact occurs, rinse thoroughly and seek medical attention if necessary.</p>
  </div>
  <div class="expiry-box" style="left:1188px;top:939px;width:168px;height:54px"></div>
  <div class="batch-box" style="left:1188px;top:998px;width:168px;height:53px"></div>

  <div class="brand-name" style="left:852px;top:1100px">Nestwell &amp;<br>Rinse</div>
  <div class="product-tag" style="left:985px;top:1099px;width:260px;height:42px">DISHWASHING SHEETS</div>

  <div class="wave-band" role="img" aria-label="Flowing ocean wave lines" style="left:987px;top:1155px;width:326px;height:48px"></div>
  <div class="scent-name" style="left:928px;top:1204px">OCEAN<br>BREEZE</div>
  <div class="wave-band" role="img" aria-label="Flowing ocean wave lines" style="left:795px;top:1305px;width:327px;height:48px"></div>

  <div class="count-number" style="left:1225px;top:1278px">80</div>
  <div class="count-label" style="left:1226px;top:1334px;width:72px;height:19px">SHEETS</div>

  <div class="claim-badge" role="img" aria-label="Circular badge: Tough on grease, with bubbles" style="left:840px;top:1354px"></div>
  <div class="claim-badge" role="img" aria-label="Circular badge: Gentle on the environment, with leaf" style="left:1007px;top:1354px"></div>
  <div class="claim-badge" role="img" aria-label="Circular badge: Simple, clean, and convenient, with sparkles" style="left:1174px;top:1354px"></div>

  <div class="benefit-strip" style="left:820px;top:1451px;width:468px;height:40px">
    <p>Harness the power of plant-based enzymes to break down stubborn grease and grime, leaving your dishes spotless without harmful residues.</p>
    <p>Ditch messy liquids and bulky pods—our sheets are an easy-to-use, space-saving solution that gets the job done with zero fuss.</p>
  </div>

  <div class="dim-label vertical" style="left:424px;top:432px">35,5</div>
  <div class="dim-label vertical" style="left:430px;top:718px">115</div>
  <div class="dim-label vertical" style="left:430px;top:1007px">40</div>
  <div class="dim-label vertical" style="left:430px;top:1318px">115</div>
  <div class="dim-label vertical" style="left:424px;top:1592px">39,5</div>
  <div class="dim-label" style="left:605px;top:1712px">39</div>
  <div class="dim-label" style="left:1018px;top:1712px">180</div>
  <div class="dim-label" style="left:1452px;top:1712px">39</div>
</div>
</body>
</html>
```